Football (soccer) board game app design

Hi,

We are a start up looking for a gameplay design for an app. It is a football trivia app that consists of four main screens; login/register, main navigation, gameplay, question.

OVERALL:
We want our app to be kept in a dark theme. Black or very dark gray is preferable, with a couple of nice colors to give it a stylish touch. We like flat designs, but are open for ideas within the general structure design. The logo can be used in the app, but feel free to improve it you feel you can. In the attached material we have tried to outline some of our ideas and other designs friends have helped us make.

LOGIN/REGISTER:
We want a simple login. Email, password, Chatterly login and the possibility to register a new user. Live search check whether the email is valid and free, and there is also live validation of passwords. If this could be incorporated in the design it would be nice.

MAIN NAVIGATION:
In the main navigation screen we want it to be divided into tabs. A home, my games, my categories and a ranking tab. In the top bar it should be possible to search for categories as well as there should be a button to go to settings.

The Home tab
In the home tab we want a "Quick Play" button, and a list of featured categories. A category can be unlocked or locked, which should be illustrated somehow. When a category is tapped it should divide the block into a left and right tap area, where the user can choose to "Beat to unlock" or "Buy to unlock" if locked and "Practice" or "Challenge Friend" if already unlocked.

The My Games tab
In the my games tab, the current games should be divided into three lists. First "your turn", then "opponents turn" and finally "finished games".

The My Categories tab
This tab should include a list of categories, which the user have bought, but as of design it is fairly similar to the blocks in home tab. So not much different here.

The Ranking tab
Ranking should show a set of leaderboards; Today, This Week, This Month, etc. The row in a leaderboard should have teamname and a win percentage.

GAMEPLAY:
The gameplay is inspired by an old football (soccer) board game from the 1950's, and our gameplay consists of three core elements; a football (soccer) pitch, 11 players and a scoreboard.

The football (soccer) pitch
What we need is a pitch seen from behind the goal line. The important issue here, is the perspective, as we want 11 players on the field formed as a 4-3-3 formation, being 1 goalkeeper, 4 defenders, 3 midfielder and 3 strikers. They should all be touchable without overlap. In the other end we want a goal that should be touchable as well. The goal in the nearest end do not have to be visible. Due to the perspective of the field and the fact that players and goal should be touchable, of course give you the opportunity to play around with the proportions of both players and goal. We rather want a large goal being out of proportions, than a small goal with a tiny tap area. Around the field (sidelines and beside the goal) we would like advertising banners like seen on a real stadium.

The players
As mentioned we want 11 players in a 4-3-3 formation. The players should be attached to the board with springs as seen on some of the very old board games, where you could flick the player to pass the ball. This also means that we want the players to be placed in an indentation for the ball to fall into and it would be very cool if you could illustrate the player with the ball, as being pulled back to one of the sides, just enough to see the ball at his feet. The players should be large enough for a user to tap them, hence it would also be beneficial if they are not overlapping. For a start we would like to see the players in a blue shirt and white shorts (socks are not necessary as they are placed on a spring).

Scoreboard
On the scoreboard above the field, we need information such as the names of the two teams (could be FC Brightmoor and Tall Oak Rovers), the score (2-1), minutes played (42), and which half (1st). We also want a progress bar that illustrates how many moves you have used ranging from 0-5. The scoreboard could be inspired from the ones seen around stadiums across the world, but feel free to improvise.

What We Are Looking for
We are looking for full PSD and AI files so we can use them to make minor changes like colors on shirts and shorts, colors on pitch, etc. We really want you to be innovative and inspire us, as we are not designers ourselves. In the attached files, we have tried to sketch out a design that covers our initial ideas. We are looking for a professional look, and having the players and field look like a real board game would just be awesome. A combination of the look from the realistic pitch with advertising banners around it, the idea of our spring-players and the initial thoughts of a design illustrated in our sketch, should help you along. Flat design, cartoonish or somewhere in between is up to you, we just want you to impress and make "wow"-feeling.

QUESTION:
The final screen should display a question with four possible answers. There should be a green/checkmark when correct answer, and a red/cross if incorrect.

That's all. We are looking very much forward to see your designs!
Updates

Hi all,

We have changed the terms of the contest to now have a guaranteed payment, and we are really looking forward to see your designs! Good luck.

/ Mikkel and Anders

By request we have now uploaded an AI-file with the logo for you to play around with. We are looking forward to see your designs.

/ Mikkel and Anders

Reason: Hi designers, We are really happy with the progress being made, and are looking forward to see some of the designs that are still work in progress. However the amount of designs received, has not reached our expectations yet. Therefore we are extending the deadline for seven more days, so designers, that are still working on their designs can continue their work without a stressing deadline in the horizon. Good luck to all of you. We are looking very much forward to see, what you are able to produce. Best regards, Mikkel and Anders

Reason: Hi all, We still have a lot of designers in the competition , who are battling to finish their designs, therefore we have decided to extend the deadline once more. Good luck to all of you!

Target Market(s)

Football (soccer) fans

Industry/Entity Type

Advertising

```html
<!DOCTYPE html>
<html lang="en">
<head>
<meta charset="utf-8">
<title>kickquizzer – Login</title>
<link rel="stylesheet" href="https://fonts.googleapis.com/css2?family=Raleway:wght@200;300;400&family=Open+Sans:wght@400;600&display=swap">
<style>
  :root {
    --page-bg: #05070a;
    --screen-bg: #0b1018;
    --screen-deep: #06090e;
    --accent: #00b6f2;
    --accent-text: #19aee8;
    --line: #c9d2dc;
    --white: #ffffff;
    --social: #4a62a1;
    --social-edge: #3b5290;
    --glow: #17324d;
  }
  * { box-sizing: border-box; margin: 0; padding: 0; }
  html, body {
    width: 694px; height: 1200px; overflow: hidden;
    background: var(--page-bg);
    font-family: "Raleway", "Helvetica Neue", Arial, sans-serif;
  }
  .app-screen {
    position: absolute; left: 0; top: 80px;
    width: 694px; height: 1041px; overflow: hidden;
    background: radial-gradient(ellipse at 75% 45%, #10233a 0%, var(--screen-bg) 45%, var(--screen-deep) 100%);
  }
  .hero-art {
    position: absolute; left: 0; top: 150px; width: 694px; height: 720px;
    background:
      radial-gradient(ellipse 200px 160px at 130px 320px, rgba(70,95,125,.35), transparent 70%),
      radial-gradient(ellipse 320px 120px at 520px 280px, rgba(40,110,170,.28), transparent 70%),
      radial-gradient(ellipse 400px 140px at 420px 620px, rgba(30,80,130,.22), transparent 70%);
  }
  .status-bar {
    position: absolute; left: 0; top: 0; width: 694px; height: 36px;
    background: #000; color: var(--white);
    font-family: "Open Sans", Arial, sans-serif; font-weight: 600; font-size: 25px;
  }
  .status-bar .carrier { position: absolute; left: 8px; top: 2px; display: flex; align-items: center; gap: 5px; }
  .status-bar .clock { position: absolute; left: 0; right: 0; top: 1px; text-align: center; }
  .status-bar .indicators { position: absolute; right: 8px; top: 2px; display: flex; align-items: center; gap: 8px; }
  .brand {
    position: absolute; left: 0; right: 0; top: 140px; text-align: center;
    color: var(--white); font-weight: 200; font-size: 52px; letter-spacing: 1px;
  }
  .field {
    position: absolute; left: 101px; width: 496px; height: 44px;
    border-bottom: 1.5px solid var(--line);
    color: var(--accent-text); font-size: 23px; font-weight: 300;
    line-height: 44px;
  }
  .field--email { top: 273px; }
  .field--password { top: 361px; }
  .btn {
    position: absolute; display: flex; align-items: center; justify-content: center;
    background: var(--accent); color: var(--white);
    font-weight: 300; font-size: 25px; letter-spacing: .5px;
  }
  .btn--login { left: 101px; top: 445px; width: 496px; height: 58px; }
  .divider-or {
    position: absolute; left: 0; right: 0; top: 529px; text-align: center;
    color: var(--white); font-size: 25px; font-weight: 400;
  }
  .btn--social {
    position: absolute; left: 169px; top: 585px; width: 358px; height: 69px;
    background: var(--social); border: 1px solid var(--social-edge); border-radius: 6px;
    display: flex; align-items: center; color: var(--white);
    font-family: "Open Sans", Arial, sans-serif; font-size: 27px;
  }
  .btn--social .social-mark {
    width: 69px; height: 100%; border-right: 1px solid var(--social-edge);
    display: flex; align-items: center; justify-content: center;
  }
  .btn--social .social-mark span { width: 26px; height: 26px; background: var(--white); border-radius: 4px; }
  .btn--social .label { flex: 1; text-align: center; }
  .signup-prompt {
    position: absolute; left: 32px; top: 738px;
    color: var(--accent-text); font-size: 26px; font-weight: 400;
  }
  .btn--signup { left: 435px; top: 726px; width: 217px; height: 58px; }
</style>
</head>
<body>
  <main class="app-screen">
    <div class="hero-art" role="img" aria-label="Background photo of a footballer mid-kick surrounded by blue light streaks and sparkles"></div>

    <header class="status-bar">
      <div class="carrier">
        <svg width="34" height="18" viewBox="0 0 34 18" aria-hidden="true">
          <rect x="0" y="12" width="5" height="6" fill="#fff"/>
          <rect x="7" y="9" width="5" height="9" fill="#fff"/>
          <rect x="14" y="6" width="5" height="12" fill="#fff"/>
          <rect x="21" y="3" width="5" height="15" fill="#fff"/>
          <rect x="28" y="0" width="5" height="18" fill="#fff"/>
        </svg>
        <span>Cellio</span>
      </div>
      <div class="clock">4:20 PM</div>
      <div class="indicators">
        <svg width="22" height="22" viewBox="0 0 22 22" aria-hidden="true"><path d="M21 1 1 10l9 2 2 9z" fill="#fff"/></svg>
        <svg width="14" height="24" viewBox="0 0 14 24" aria-hidden="true"><path d="M1 7l12 10-6 5V2l6 5L1 17" fill="none" stroke="#fff" stroke-width="2"/></svg>
        <svg width="30" height="20" viewBox="0 0 30 20" aria-hidden="true"><rect x="1" y="8" width="28" height="10" rx="2" fill="none" stroke="#fff" stroke-width="2"/><rect x="18" y="2" width="8" height="7" rx="3" fill="none" stroke="#fff" stroke-width="2"/></svg>
        <span>100%</span>
        <svg width="40" height="20" viewBox="0 0 40 20" aria-hidden="true"><rect x="1" y="2" width="34" height="16" rx="3" fill="none" stroke="#fff" stroke-width="2"/><rect x="4" y="5" width="28" height="10" fill="#fff"/><rect x="36" y="7" width="3" height="6" fill="#fff"/></svg>
      </div>
    </header>

    <h1 class="brand">kickquizzer</h1>

    <div class="field field--email">EMAIL</div>
    <div class="field field--password">PASSWORD</div>

    <div class="btn btn--login">LOGIN</div>
    <div class="divider-or">OR</div>

    <div class="btn--social">
      <div class="social-mark"><span></span></div>
      <div class="label">Login with Chatterly</div>
    </div>

    <p class="signup-prompt">DON’T HAVE AN ACCONT YET?</p>
    <div class="btn btn--signup">SIGN UP</div>
  </main>
</body>
</html>
```